Trade show display

All-
We are designing a trade show display. This is a 10' display that also includes a display stand (a mini table top wrap).
Please see the two images (example stand and example wall) of an example FINISHED product. You can also refer to the specs.pdf for the actual dimensions you'll need to design the product.
We've also attached our logo and our corporate font (harabara).
Please take a quick look at our website (rotaplume.com) and our Friendwall.com/rotaplume to get a quick feel for our product. We're an app that automates the process of scheduling employees for catering companies.
Here's what we want to communicate:
1. We're free
2. We're easy to use
3. We're made specifically for caterers
Our slogan is:
the UNscheduler
Bright colors are good. We don't want any stock art or images of people or really much images at all, if any. Just nice typography with good supporting shapes. Just focus on the typography to communicate the message with colored background to separate the ideas.
PLEASE MAKE THE TYPOGRAPHY LARGE! You should be able to read this from far away! No clutter, no small text, and no text towards the bottom! THINK SIMPLICITY!
Our target market is catering company (as in caterers of food for parties, weddings, etc) owners or managers. Design should be hip and trendy looking since we're a technology business but very clear and easy to read and understand.
Catering

```html
<!DOCTYPE html>
<html lang="en">
<head>
<meta charset="utf-8">
<title>rotaplume – trade show display</title>
<link rel="stylesheet" href="https://fonts.googleapis.com/css2?family=Source+Sans+3:wght@300;400;700&display=swap">
<style>
  :root {
    --charcoal: #434142;
    --slate: #6b7480;
    --mist: #d3d3d4;
    --paper: #ffffff;
    --ink: #2f2f30;
    --copy: #5e5e61;
    --copy-soft: #6f6f72;
    --guide-cyan: #3fb6e0;
    --guide-grey: #b9bcc0;
    --bleed-red: #c0485a;
    --accent: #2f8fd8;
    --sky: #8fd0f2;
  }
  * { box-sizing: border-box; margin: 0; padding: 0; }
  html, body { width: 1200px; height: 1200px; overflow: hidden; background: var(--paper); }
  body { position: relative; font-family: "Source Sans 3", Arial, sans-serif; }

  .wall, .stand { position: absolute; overflow: hidden; }
  .wall { left: 45px; top: 38px; width: 1105px; height: 634px; }
  .band { position: absolute; left: 0; width: 100%; }
  .wall .band--header { top: 0; height: 207px; background: var(--charcoal); }
  .wall .band--gap { top: 207px; height: 8px; background: var(--paper); }
  .wall .band--headline { top: 215px; height: 185px; background: var(--slate); }
  .wall .band--features { top: 400px; height: 215px; background: var(--mist); }
  .wall .band--footer { top: 615px; height: 19px; background: var(--charcoal); }

  .bleed-line { position: absolute; left: 45px; top: 38px; width: 1105px; height: 634px; border: 1px solid var(--bleed-red); pointer-events: none; }
  .safe-area { position: absolute; border: 1px solid var(--guide-cyan); pointer-events: none; }
  .wall-safe { left: 160px; top: 46px; width: 876px; height: 618px; }
  .column-guide { position: absolute; top: 38px; width: 1px; height: 634px; background: var(--guide-grey); opacity: .7; }

  .brand { position: absolute; text-align: center; }
  .brand-mark { display: block; margin: 0 auto; width: 46px; height: 46px; background: var(--accent); border-radius: 6px; }
  .brand-name { display: block; font-weight: 700; letter-spacing: -0.5px; line-height: 1; }
  .brand-slogan { display: block; font-weight: 400; line-height: 1; letter-spacing: 1px; }
  .brand-slogan strong { font-weight: 700; }
  .wall .brand { left: 0; width: 100%; top: 34px; }
  .wall .brand-name { color: var(--paper); font-size: 48px; margin-top: 18px; }
  .wall .brand-slogan { color: var(--sky); font-size: 26px; margin-top: 10px; }
  .wall-url { position: absolute; left: 0; width: 100%; top: 617px; text-align: center; font-size: 12px; line-height: 15px; color: #d6d6d8; }

  .headline { position: absolute; left: 178px; top: 262px; font-weight: 300; font-size: 80px; line-height: 1; color: var(--paper); letter-spacing: -1px; white-space: nowrap; }
  .subline { position: absolute; right: 190px; top: 356px; font-weight: 300; font-size: 40px; line-height: 1; color: var(--paper); white-space: nowrap; }

  .feature-icon { position: absolute; top: 446px; width: 70px; height: 70px; border-radius: 50%; background: var(--slate); }
  .feature-icon svg, .mini-icon svg { width: 100%; height: 100%; display: block; }
  .feature { position: absolute; top: 524px; width: 172px; color: var(--copy); }
  .feature-title { font-weight: 400; font-size: 26px; line-height: 27px; letter-spacing: -0.3px; color: var(--ink); }
  .feature-text { font-weight: 400; font-size: 16px; line-height: 19px; color: var(--copy-soft); margin-top: 3px; }

  .stand { left: 163px; top: 735px; width: 867px; height: 408px; background: var(--paper); }
  .stand .band--header { top: 0; height: 43px; background: var(--charcoal); }
  .stand .band--base { top: 295px; height: 113px; background: var(--slate); }
  .stand-url { position: absolute; left: 0; width: 100%; top: 14px; text-align: center; font-size: 13px; line-height: 15px; color: #d6d6d8; }
  .stand .brand { left: 0; width: 100%; top: 92px; }
  .stand .brand-mark { width: 36px; height: 36px; border-radius: 4px; }
  .stand .brand-name { color: var(--ink); font-size: 38px; margin-top: 16px; }
  .stand .brand-slogan { color: var(--accent); font-size: 22px; margin-top: 10px; }
  .stand-points { position: absolute; left: 0; width: 100%; top: 225px; text-align: center; font-size: 17px; line-height: 22px; color: var(--copy); font-weight: 400; }
  .stand-safe { left: 453px; top: 748px; width: 288px; height: 383px; }
  .mini-icon { position: absolute; top: 1013px; width: 31px; height: 31px; border-radius: 50%; background: var(--slate); border: 2px solid var(--paper); }
</style>
</head>
<body>

  <section class="wall" aria-label="Trade show wall">
    <div class="band band--header"></div>
    <div class="band band--gap"></div>
    <div class="band band--headline"></div>
    <div class="band band--features"></div>
    <div class="band band--footer"></div>
    <div class="brand">
      <span class="brand-mark"></span>
      <span class="brand-name">rotaplume</span>
      <span class="brand-slogan">the <strong>UN</strong>scheduler</span>
    </div>
    <span class="wall-url">rotaplume.com</span>
  </section>

  <div class="column-guide" style="left:218px"></div>
  <div class="column-guide" style="left:408px"></div>
  <div class="column-guide" style="left:598px"></div>
  <div class="column-guide" style="left:788px"></div>
  <div class="column-guide" style="left:978px"></div>

  <h1 class="headline">The app that schedules...</h1>
  <p class="subline">...so you don't have.</p>

  <div class="feature-icon" style="left:283px">
    <svg viewBox="0 0 70 70" aria-hidden="true"><polyline points="20,36 31,47 51,24" fill="none" stroke="#fff" stroke-width="5" stroke-linecap="round" stroke-linejoin="round"/></svg>
  </div>
  <div class="feature-icon" style="left:461px">
    <svg viewBox="0 0 70 70" aria-hidden="true"><polygon points="39,14 22,38 33,38 29,56 48,30 37,30" fill="#fff"/></svg>
  </div>
  <div class="feature-icon" style="left:652px">
    <svg viewBox="0 0 70 70" aria-hidden="true"><polygon points="35,17 40.3,29.5 53.5,30.2 43.3,38.8 46.8,52 35,44.6 23.2,52 26.7,38.8 16.5,30.2 29.7,29.5" fill="none" stroke="#fff" stroke-width="3" stroke-linejoin="round"/></svg>
  </div>
  <div class="feature-icon" style="left:852px">
    <svg viewBox="0 0 70 70" aria-hidden="true"><ellipse cx="36" cy="33" rx="20" ry="15" fill="#fff"/><path d="M22 42 L17 52 L30 46 Z" fill="#fff"/></svg>
  </div>

  <article class="feature" style="left:257px">
    <h2 class="feature-title">It's Free</h2>
    <p class="feature-text">No fees. No contracts. Just sign up and go.</p>
  </article>
  <article class="feature" style="left:435px">
    <h2 class="feature-title">Easy to Use</h2>
    <p class="feature-text">Set up in minutes. Your staff learn it in seconds.</p>
  </article>
  <article class="feature" style="left:624px;width:160px">
    <h2 class="feature-title">Made for Caterers</h2>
    <p class="feature-text">Built for weddings, parties &amp; events.</p>
  </article>
  <article class="feature" style="left:820px;width:150px">
    <h2 class="feature-title">It talks</h2>
    <p class="feature-text">Texts your staff to confirm every shift.</p>
  </article>

  <div class="bleed-line"></div>
  <div class="safe-area wall-safe"></div>

  <section class="stand" aria-label="Table top stand wrap">
    <div class="band band--header"></div>
    <div class="band band--base"></div>
    <span class="stand-url">rotaplume.com</span>
    <div class="brand">
      <span class="brand-mark"></span>
      <span class="brand-name">rotaplume</span>
      <span class="brand-slogan">the <strong>UN</strong>scheduler</span>
    </div>
    <p class="stand-points">Free · Easy · Made for caterers</p>
  </section>

  <div class="mini-icon" style="left:509px">
    <svg viewBox="0 0 70 70" aria-hidden="true"><polyline points="20,36 31,47 51,24" fill="none" stroke="#fff" stroke-width="7" stroke-linecap="round" stroke-linejoin="round"/></svg>
  </div>
  <div class="mini-icon" style="left:557px">
    <svg viewBox="0 0 70 70" aria-hidden="true"><polygon points="39,12 20,39 33,39 28,58 50,29 37,29" fill="#fff"/></svg>
  </div>
  <div class="mini-icon" style="left:606px">
    <svg viewBox="0 0 70 70" aria-hidden="true"><polygon points="35,15 40.6,28.5 55,29.3 44,38.6 47.7,53 35,45 22.3,53 26,38.6 15,29.3 29.4,28.5" fill="none" stroke="#fff" stroke-width="5" stroke-linejoin="round"/></svg>
  </div>
  <div class="mini-icon" style="left:654px">
    <svg viewBox="0 0 70 70" aria-hidden="true"><ellipse cx="36" cy="32" rx="21" ry="16" fill="#fff"/><path d="M21 42 L16 53 L30 46 Z" fill="#fff"/></svg>
  </div>

  <div class="safe-area stand-safe"></div>

</body>
</html>
```